Professional, Attractive, Simple Website Needed!!

We completed the design for our logo.

We need a website built out around this.

Here are a couple samples of how we want ours formatted.

http://brvntapower.com

http://www.halvorbeam.com/lp/free-quote?LeadSource=Search%20Engine&ProgramName=webquery&experience=qual&language=en&type=brd&gclid=Xq7RTPwmEYKDLAvUHbsNQkfPZrTcGwnJuoVbXeLqHmRYdAsWtPkMcNfBYgzTrUoQJhEdWvKpYaLsZbCmNDgQwTxAoKpXbT_qkR

http://morvalo.co

Reason: Extending this deadline due to our delay in providing designers with content for each page. This is coming in next 24 hours.

Reason: Due to scheduling conflicts and extended travel delays related to Puerto Rico, the deadline has been extended. Your patience is greatly appreciated.

Reason: Travel and scheduling conflicts have made it impossible to give this project the thorough review it deserves, therefore I am extending the deadline. Thank you for your patience!

Target Market(s)

Home Owners who earn 60k + household annually

Industry/Entity Type

It Professional

Coding

Coded - Design and coding required

Number of Pages Required

5+ page

Font styles to use
Serif

Colors
34a7d8
9bcb3c

Requirements
Must have
• Simple
• Lead form Entry (Ability for visitor to enter Name, number and address for a quote)
• Sleek Design
• Professional
• Testimonials
• Use color Scheme of Design Logo Attached
Nice to have
• Video when site starts
• Like this
• https://www.vidmarrow.com/watch?v=qT8mRpXw2Ka&feature=vidm.ro
Should not have
• Should not include Commercial solar
• Should not include wind power

```html
<!DOCTYPE html>
<html lang="en">
<head>
<meta charset="utf-8">
<title>Sunvale Energy</title>
<link rel="stylesheet" href="https://fonts.googleapis.com/css2?family=Roboto:ital,wght@0,300;0,400;0,500;0,700;1,400&display=swap">
<style>
:root{
  --blue:#34a7d8;
  --green:#9bcb3c;
  --dark:#262a2f;
  --footer:#2e2e2e;
  --ink:#444;
  --muted:#666;
  --white:#fff;
}
*{box-sizing:border-box;margin:0;padding:0}
html,body{width:674px;height:1200px;overflow:hidden;background:#fff}
body{position:relative;font-family:'Roboto',Arial,sans-serif;color:var(--ink)}
.abs{position:absolute}
.center{left:0;width:674px;text-align:center}

/* hero */
.hero{left:0;top:0;width:674px;height:347px;
  background:linear-gradient(160deg,#e9e6e0 0%,#9aa3a8 14%,#3d4a5c 38%,#2b3950 60%,#4c5870 80%,#8e7a66 100%)}
.brand{left:90px;top:10px;display:flex;align-items:center;gap:5px}
.brand-mark{width:22px;height:22px;border-radius:50%;border:2px solid var(--green)}
.brand-name{font-size:11px;font-weight:500;color:var(--blue);line-height:1.1;width:50px}
.social{top:7px;left:440px;display:flex;gap:2px}
.social span{width:14px;height:14px;border-radius:50%;border:1px solid var(--blue)}
.call{left:513px;top:6px;display:flex;gap:5px;align-items:center;border-left:1px solid var(--blue);padding-left:8px}
.call-icon{width:15px;height:15px;border-radius:50%;border:1px solid var(--blue);display:flex;align-items:center;justify-content:center}
.call-text{font-size:5px;color:var(--blue);line-height:1.3}
.call-text b{display:block;font-size:7px;font-weight:700}
.nav{top:38px;left:352px;display:flex;gap:18px;font-size:6.2px;color:#222;letter-spacing:.3px}
.nav .active{color:var(--blue);border-bottom:1px solid var(--blue);padding-bottom:6px}
.hero-title{top:110px;font-size:21px;font-weight:700;color:#fff;letter-spacing:1px}
.hero-title em{font-style:normal;background:#fff;color:var(--blue);padding:2px 5px}
.hero-sub{top:151px;left:187px;width:300px;font-size:7.6px;line-height:1.35;color:#f2f2f2;text-align:center;letter-spacing:.3px}
.btn-learn{left:289px;top:201px;width:96px;height:25px;background:var(--green);color:#fff;font-size:7.5px;letter-spacing:.6px;display:flex;align-items:center;justify-content:center;gap:4px}

/* quote */
.quote-tab{left:290px;top:289px;width:93px;height:20px;background:var(--blue);color:#fff;font-size:7px;font-weight:500;display:flex;align-items:center;justify-content:center}
.quote-form{left:90px;top:309px;width:493px;height:76px;background:var(--blue)}
.field{position:absolute;top:21px}
.field label{display:block;font-size:5.5px;font-weight:700;color:#fff;margin-bottom:5px}
.field .input{width:120px;height:24px;border:1px solid #e8f4fb;border-radius:2px}
.btn-submit{position:absolute;left:388px;top:32px;width:96px;height:24px;background:var(--green);color:#fff;font-size:5.5px;font-weight:700;display:flex;align-items:center;justify-content:center;border-radius:2px}

/* section heads */
.sec-title{font-size:13px;font-weight:300;letter-spacing:1px;color:var(--blue)}
.sec-title .g{color:var(--green)}
.sec-rule{width:18px;height:1px;background:var(--green);margin:4px auto 0}
.sec-sub{font-size:5.8px;letter-spacing:1.6px;color:#555}

/* cards */
.card{top:473px;width:156px;height:148px;background:#fff;box-shadow:0 0 4px rgba(0,0,0,.12);text-align:center}
.card.featured{background:var(--green);color:#fff}
.card-icon{width:50px;height:50px;margin:16px auto 0;border-radius:50%;background:#555}
.card.featured .card-icon{background:#fff;border-radius:4px;width:62px;height:34px;margin-top:24px}
.card h3{font-size:9.5px;font-weight:400;letter-spacing:2px;margin-top:16px;color:#444}
.card.featured h3{color:#fff;margin-top:24px}
.card p{font-size:6.2px;line-height:1.6;color:#555;margin:4px auto 0;width:120px}
.card.featured p{color:#fff}
.btn-read{display:inline-block;margin-top:9px;width:46px;height:15px;line-height:15px;background:#555;color:#fff;font-size:5.5px}
.card.featured .btn-read{background:#fff;color:#555}

/* testimonial */
.clients{left:0;top:654px;width:674px;height:259px;
  background:linear-gradient(135deg,#1f242b 0%,#2e3640 45%,#252b33 75%,#1c2026 100%)}
.avatar{left:307px;top:733px;width:60px;height:60px;border-radius:50%;border:2px solid #fff;background:linear-gradient(180deg,#b8a79a,#8a7a6e)}
.quote-text{left:205px;top:810px;width:264px;font-size:7.2px;line-height:1.4;color:#eee;text-align:center}
.qmark{font-size:20px;font-weight:700;color:var(--blue);line-height:1}
.client-name{top:847px;font-size:6.5px;font-style:italic;color:var(--blue);letter-spacing:.5px}
.dots{top:884px;left:326px;display:flex;gap:3px}
.dots span{width:5px;height:5px;border-radius:50%;background:#fff}
.dots span.on{background:var(--blue)}

/* newsletter */
.news-input{left:171px;top:995px;width:266px;height:23px;border:1px solid #ccc;font-size:6px;color:#666;padding:8px 5px}
.btn-sub{left:437px;top:995px;width:60px;height:23px;background:var(--green);color:#fff;font-size:5.8px;display:flex;align-items:center;justify-content:center;gap:4px}

/* footer */
.footer{left:0;top:1040px;width:674px;height:160px;background:var(--footer);color:#bbb}
.f-brand{position:absolute;left:90px;top:27px;display:flex;align-items:center;gap:4px}
.f-brand .brand-mark{border-color:#ccc;width:18px;height:18px}
.f-brand .brand-name{color:#ccc;font-size:9px}
.f-about{position:absolute;left:90px;top:69px;width:114px;font-size:5.8px;line-height:1.55}
.f-col{position:absolute;top:27px}
.f-col h4{font-size:6.8px;font-weight:500;color:#ddd}
.f-col h4::after{content:"";display:block;width:12px;height:1px;background:var(--blue);margin-top:3px}
.f-col ul{list-style:none;margin-top:15px}
.f-col li{font-size:6px;height:14px;padding-left:15px;position:relative}
.f-col li::before{content:"";position:absolute;left:0;top:2px;width:3px;height:3px;border-radius:50%;background:#ddd}
.contact li{padding-left:15px;line-height:1.5;height:auto;margin-bottom:6px}
.contact li::before{display:none}
.contact svg{position:absolute;left:0;top:1px}
.f-rule{position:absolute;left:90px;top:127px;width:493px;height:1px;background:#444}
.copyright{position:absolute;top:140px;left:0;width:674px;text-align:center;font-size:5.8px;color:#aaa}
</style>
</head>
<body>

<header class="abs hero" role="img" aria-label="Photo of rooftop solar panels in warm sunlight">
</header>
<div class="abs brand"><span class="brand-mark"></span><span class="brand-name">SUNVALE ENERGY</span></div>
<div class="abs social"><span></span><span></span><span></span><span></span></div>
<div class="abs call">
  <span class="call-icon"><svg width="7" height="7" viewBox="0 0 24 24"><path fill="#34a7d8" d="M6.6 10.8a15 15 0 0 0 6.6 6.6l2.2-2.2c.3-.3.7-.4 1-.2 1.1.4 2.3.6 3.6.6.6 0 1 .4 1 1V20c0 .6-.4 1-1 1A17 17 0 0 1 3 4c0-.6.4-1 1-1h3.5c.6 0 1 .4 1 1 0 1.3.2 2.5.6 3.6.1.3 0 .7-.2 1z"/></svg></span>
  <span class="call-text">CALL US AT<b>999-999-9999</b></span>
</div>
<nav class="abs nav"><span class="active">HOME</span><span>ABOUT US</span><span>SERVICES</span><span>HOW IT WORK</span><span>CONTACT US</span></nav>
<h1 class="abs center hero-title">SAVING <em>ENERGY</em></h1>
<p class="abs hero-sub">THERE ARE MANY VARIATIONS OF PASSAGES OF LOREM IPSUM AVAILABLE, BUT THE MAJORITY HAVE SUFFERED ALTERATION IN SOME FORM, BY INJECTED HUMOUR</p>
<div class="abs btn-learn">LEARN MORE <svg width="8" height="8" viewBox="0 0 10 10"><circle cx="5" cy="5" r="5" fill="#fff"/><path d="M3.5 2.5 6 5 3.5 7.5" stroke="#9bcb3c" stroke-width="1.4" fill="none"/></svg></div>

<div class="abs quote-tab">GET FREE QUOTE</div>
<form class="abs quote-form">
  <div class="field" style="left:8px"><label>NAME</label><div class="input"></div></div>
  <div class="field" style="left:135px"><label>PHONE</label><div class="input"></div></div>
  <div class="field" style="left:262px"><label>ADDRESS</label><div class="input"></div></div>
  <div class="btn-submit">SUBMIT</div>
</form>

<section>
  <h2 class="abs center sec-title" style="top:413px">ABOUT US<div class="sec-rule"></div></h2>
  <p class="abs center sec-sub" style="top:439px">LOREM IPSUM IS SIMPLY DUMMY TEXT OF THE PRINTING</p>
  <article class="abs card" style="left:90px">
    <div class="card-icon" role="img" aria-label="Energy-saving light bulb icon"></div>
    <h3>ENERGY ANALYSIS</h3>
    <p>Lorem ipsum dolor sit amet, consectetur adipiscing elit. Etiam placerat</p>
    <span class="btn-read">READ MORE</span>
  </article>
  <article class="abs card featured" style="left:259px">
    <div class="card-icon" role="img" aria-label="House with solar panel icon"></div>
    <h3>NEW SOLUTIONS</h3>
    <p>Lorem ipsum dolor sit amet, consectetur adipiscing elit. Etiam placerat</p>
    <span class="btn-read">READ MORE</span>
  </article>
  <article class="abs card" style="left:427px">
    <div class="card-icon" role="img" aria-label="Globe with leaf icon"></div>
    <h3>GO GREEN</h3>
    <p>Lorem ipsum dolor sit amet, consectetur adipiscing elit. Etiam placerat</p>
    <span class="btn-read">READ MORE</span>
  </article>
</section>

<section class="abs clients" role="img" aria-label="Dark photo of a technician installing solar panels"></section>
<h2 class="abs center sec-title" style="top:675px">CLIENT <span class="g">SPEAK</span><div class="sec-rule"></div></h2>
<p class="abs center sec-sub" style="top:701px;color:#eee">LOREM IPSUM IS SIMPLY DUMMY TEXT OF THE PRINTING</p>
<div class="abs avatar" role="img" aria-label="Client portrait"></div>
<span class="abs qmark" style="left:196px;top:806px">&ldquo;</span>
<p class="abs quote-text">Vivamus at pretium mauris. Morbi enim massa, viverra at risus sed, euismod dignissim orci.Quisque convallis a libero vitae euismod.Nullam et ex et</p>
<span class="abs qmark" style="left:458px;top:819px">&rdquo;</span>
<p class="abs center client-name">DANIEL ROWE</p>
<div class="abs dots"><span></span><span class="on"></span><span></span></div>

<section>
  <h2 class="abs center sec-title" style="top:946px">SUSCRIBE <span class="g">NEWSLETTER</span><div class="sec-rule"></div></h2>
  <p class="abs center sec-sub" style="top:972px">LOREM IPSUM IS SIMPLY DUMMY TEXT OF THE PRINTING</p>
  <div class="abs news-input">Enter your email</div>
  <div class="abs btn-sub"><svg width="7" height="5" viewBox="0 0 14 10"><rect x=".5" y=".5" width="13" height="9" fill="none" stroke="#fff"/><path d="M.5.5 7 6 13.5.5" fill="none" stroke="#fff"/></svg>SUBSCRIBE</div>
</section>

<footer class="abs footer">
  <div class="f-brand"><span class="brand-mark"></span><span class="brand-name">SUNVALE ENERGY</span></div>
  <p class="f-about">There are many variations of passages of Lorem Ipsum available, but the majority have suffered alteration in some form, by injected humour, or randomised words which don't look even slightly believable.</p>
  <div class="f-col" style="left:218px"><h4>INFORMATION</h4><ul><li>Home</li><li>About us</li><li>Services</li><li>How it works</li></ul></div>
  <div class="f-col" style="left:343px"><h4>MY ACCOUNT</h4><ul><li>Privacy Policya</li><li>Terms of Use</li><li>Contact us</li><li>Site Map</li></ul></div>
  <div class="f-col contact" style="left:469px;width:115px"><h4>GET IN TOUCH</h4><ul>
    <li><svg width="5" height="7" viewBox="0 0 10 14"><path fill="#ddd" d="M5 0a5 5 0 0 0-5 5c0 4 5 9 5 9s5-5 5-9a5 5 0 0 0-5-5zm0 7a2 2 0 1 1 0-4 2 2 0 0 1 0 4z"/></svg>There are many variations of passages of Lorem Ipsum available</li>
    <li><svg width="6" height="6" viewBox="0 0 24 24"><path fill="#ddd" d="M6.6 10.8a15 15 0 0 0 6.6 6.6l2.2-2.2c.3-.3.7-.4 1-.2 1.1.4 2.3.6 3.6.6.6 0 1 .4 1 1V20c0 .6-.4 1-1 1A17 17 0 0 1 3 4c0-.6.4-1 1-1h3.5c.6 0 1 .4 1 1 0 1.3.2 2.5.6 3.6.1.3 0 .7-.2 1z"/></svg>999-999-9999</li>
    <li><svg width="7" height="5" viewBox="0 0 14 10"><rect x=".5" y=".5" width="13" height="9" fill="none" stroke="#ddd"/><path d="M.5.5 7 6 13.5.5" fill="none" stroke="#ddd"/></svg>info@yourdomain.com</li>
  </ul></div>
  <div class="f-rule"></div>
  <p class="copyright">Copyright © 2017 Sunvale Energy. All rights reserved.</p>
</footer>

</body>
</html>
```